Website Design for Bright Path Learning

The business is called Bright Path Learning - a Drug & Alcohol Education program for Sydney school kids. I wish to create a simple online business card which covers who we are, the programs we offer and why they should choose us. I would like the business page to be very colourful and school-friendly, but with the seriousness of alcohol and drug use. I have attached some pictures and logos for the business. The programs are called 'clear road' for high school, and 'step ahead' for primary school. The logo is black & white. There is also a photo of the manager with some kids.

```html
<!DOCTYPE html>
<html lang="en">
<head>
<meta charset="utf-8">
<title>Bright Path Learning – Mobile Home</title>
<link rel="stylesheet" href="https://fonts.googleapis.com/css2?family=Arvo:wght@400;700&family=Open+Sans:wdth,wght@75,400;75,600&display=swap">
<style>
  :root {
    --stage: #000000;
    --paper: #ffffff;
    --ink: #231f20;
    --teal: #2ecbd6;
    --teal-deep: #1fb3bd;
    --label: #1fb0b9;
    --social: #e4dfd5;
    --white: #ffffff;
  }
  * { margin: 0; padding: 0; box-sizing: border-box; }
  html, body { width: 1200px; height: 1000px; overflow: hidden; background: var(--stage); }
  body { position: relative; font-family: "Arvo", "Rockwell", serif; color: var(--ink); }

  .stage-note {
    position: absolute; top: 90px; width: 240px; text-align: center;
    color: var(--white); font-size: 16px; line-height: 21.5px;
  }
  .stage-note h2 { font-size: 16px; font-weight: 400; margin-bottom: 21px; }
  .stage-note--left { left: 64px; }
  .stage-note--right { left: 905px; }

  .mobile-page {
    position: absolute; left: 366px; top: 0; width: 470px; height: 1000px;
    background: var(--paper); overflow: hidden;
  }
  .site-header { position: relative; height: 260px; text-align: center; }
  .brand-name {
    position: absolute; top: 30px; left: 0; width: 100%;
    font-family: "Open Sans", sans-serif; font-stretch: 75%; font-weight: 600;
    font-size: 74px; line-height: 96px; color: var(--ink); letter-spacing: 1px;
  }
  .social-links { position: absolute; top: 135px; left: 201px; display: flex; gap: 8px; }
  .social-links span { width: 30px; height: 30px; border-radius: 50%; background: var(--social); display: block; }
  .contact-phone, .contact-email {
    position: absolute; left: 0; width: 100%;
    font-family: "Open Sans", sans-serif; font-stretch: 75%; color: var(--ink);
  }
  .contact-phone { top: 168px; font-size: 30px; }
  .contact-email { top: 201px; font-size: 28px; }

  .menu-bar {
    position: absolute; top: 260px; left: 0; width: 468px; height: 40px;
    background: var(--teal); text-align: center; font-size: 17px; line-height: 38px;
  }

  .tagline {
    position: absolute; top: 300px; left: 0; width: 100%; height: 80px;
    font-family: "Open Sans", sans-serif; font-stretch: 75%; font-size: 25px; text-align: center;
  }
  .tagline p { position: absolute; top: 27px; width: 100%; }
  .tagline .quote-mark {
    position: absolute; top: 8px; font-family: "Arvo", serif; font-weight: 700; font-size: 40px; line-height: 40px;
  }
  .tagline .quote-open { left: 32px; }
  .tagline .quote-close { left: 413px; }

  .feature-grid {
    position: absolute; top: 380px; left: 1px; width: 468px; height: 449px; background: var(--teal);
  }
  .feature { position: absolute; width: 200px; text-align: center; }
  .feature-ring {
    position: absolute; left: 28px; top: 0; width: 145px; height: 145px; border-radius: 50%;
    background: var(--teal-deep);
  }
  .feature-image {
    position: absolute; left: 10px; top: 10px; width: 125px; height: 125px; border-radius: 50%;
  }
  .feature-label {
    position: absolute; top: 155px; left: 0; width: 200px; height: 18px; border-radius: 3px;
    background: var(--label); color: var(--white); font-size: 13px; line-height: 18px;
  }
  .feature--about { left: 19px; top: 20px; }
  .feature--step { left: 252px; top: 20px; }
  .feature--clear { left: 18px; top: 226px; }
  .feature--why { left: 251px; top: 226px; }

  .img-portrait { background: radial-gradient(circle at 50% 45%, #3a3a3a 0%, #5b5f66 40%, #d8d4cf 75%); }
  .img-step { background: linear-gradient(135deg, #c7d93a 0%, #2ecbd6 55%, #e9c27a 100%); }
  .img-clear { background: linear-gradient(135deg, #ffffff 0%, #e8f4ea 60%, #7cc35a 100%); }
  .img-group { background: linear-gradient(160deg, #c9ccd0 0%, #6b8fb8 50%, #9b9a93 100%); }

  .welcome { position: absolute; top: 850px; left: 22px; width: 426px; text-align: center; }
  .welcome h1 { font-size: 25px; font-weight: 400; margin-bottom: 18px; }
  .welcome p { font-size: 13px; line-height: 17px; }
</style>
</head>
<body>
  <aside class="stage-note stage-note--left">
    <h2>Mobile Version</h2>
    <p>These black parts would not be visible on the actual site.</p>
  </aside>
  <aside class="stage-note stage-note--right">
    <h2>Mobile Version</h2>
    <p>These black parts would not be visible on the actual site.</p>
  </aside>

  <main class="mobile-page">
    <header class="site-header">
      <div class="brand-name">Bright Path</div>
      <div class="social-links"><span></span><span></span></div>
      <div class="contact-phone">02 5550 1234</div>
      <div class="contact-email">info@brightpathlearning.com</div>
    </header>

    <nav class="menu-bar">Menu</nav>

    <section class="tagline">
      <span class="quote-mark quote-open">“</span>
      <p>Education Programs for Lifelong Enjoyment</p>
      <span class="quote-mark quote-close">”</span>
    </section>

    <section class="feature-grid">
      <div class="feature feature--about">
        <div class="feature-ring"><div class="feature-image img-portrait" role="img" aria-label="Photo of the program manager seated against a light wall"></div></div>
        <div class="feature-label">About us</div>
      </div>
      <div class="feature feature--step">
        <div class="feature-ring"><div class="feature-image img-step" role="img" aria-label="Step Ahead program artwork with a book and paintbrush"></div></div>
        <div class="feature-label">Step Ahead Program</div>
      </div>
      <div class="feature feature--clear">
        <div class="feature-ring"><div class="feature-image img-clear" role="img" aria-label="Clear Road program artwork"></div></div>
        <div class="feature-label">Clear Road Program</div>
      </div>
      <div class="feature feature--why">
        <div class="feature-ring"><div class="feature-image img-group" role="img" aria-label="Photo of the manager standing with a group of kids"></div></div>
        <div class="feature-label">Why choose us</div>
      </div>
    </section>

    <section class="welcome">
      <h1>Welcome to Bright Path Learning</h1>
      <p>Lorem ipsum dolor sit amet, consectetur adipiscing elit. Pellentesque sit amet urna lacus. Nam ipsum felis, condimentum molestie consectetur ac; blandit at felis. Nulla facilisi. Sed id sapien ac massa cursus pretium et id sapien. Ut varius eros vitae turpis porttitor iaculis. Sed eget lacus eu elit rutrum eleifend sed lacinia nulla. Maecenas eu ligula a nulla placerat accumsan eget ac nunc.</p>
    </section>
  </main>
</body>
</html>
```